July 4th Postcard to existing clients

5x7 postcard wishing our clients happy 4th of July. Card should read on the back "Thank You For Being A Valued Client!. Stay Safe And Enjoy Your Independence Day Celebrations!"

Patriotic theme with fireworks is ideal. We are a law firm so should still have a feel of professionalism while still being fun since it is for a fun holiday.

```html
<!DOCTYPE html>
<html lang="en">
<head>
<meta charset="utf-8">
<title>Independence Day Postcard – Halden Law</title>
<link rel="stylesheet" href="https://fonts.googleapis.com/css2?family=Archivo+Black&family=Oswald:wght@300;400&family=Lato:wght@400&display=swap">
<style>
  :root {
    --navy: #12274a;
    --navy-deep: #0c1d38;
    --steel: #7891ad;
    --steel-dim: #6b84a0;
    --flag-red: #d0232a;
    --flag-white: #f4f4f6;
    --flag-blue: #2c2f8f;
    --statue-light: #9fb0c6;
    --statue-dark: #4f6583;
    --brand-grey: #8b9099;
    --brand-mark: #b4b8d0;
  }
  html, body {
    margin: 0;
    padding: 0;
    overflow: hidden;
    background: #ffffff;
  }
  .postcard {
    position: relative;
    width: 869px;
    height: 1200px;
    overflow: hidden;
    background:
      radial-gradient(ellipse at 45% 60%, #17305a 0%, var(--navy) 45%, var(--navy-deep) 100%);
  }
  .flag-art {
    position: absolute;
    top: 0;
    left: 0;
    width: 869px;
    height: 440px;
  }
  .headline {
    position: absolute;
    inset: 0;
    margin: 0;
    font-family: "Archivo Black", "Arial Black", sans-serif;
    font-weight: 400;
    color: var(--steel);
    line-height: 1;
    text-shadow: 3px 4px 6px rgba(0, 0, 0, 0.45);
    pointer-events: none;
  }
  .headline span { position: absolute; white-space: nowrap; }
  .headline-four  { left: 132px; top: 445px; font-size: 240px; letter-spacing: 0; }
  .headline-th    { left: 364px; top: 547px; font-size: 74px; letter-spacing: -4px; }
  .headline-of    { left: 364px; top: 601px; font-size: 74px; letter-spacing: 3px; }
  .headline-july  { left: 40px;  top: 641px; font-size: 160px; letter-spacing: 4px; }
  .subtitle {
    position: absolute;
    left: 102px;
    top: 784px;
    margin: 0;
    font-family: "Oswald", "Arial Narrow", sans-serif;
    font-weight: 300;
    font-size: 72px;
    line-height: 1;
    letter-spacing: -0.5px;
    color: var(--steel-dim);
    transform: scaleX(0.74);
    transform-origin: left top;
    white-space: nowrap;
  }
  .statue {
    position: absolute;
    left: 540px;
    top: 472px;
    width: 300px;
    height: 728px;
    border-radius: 60px 60px 0 0;
    background: linear-gradient(100deg, var(--statue-dark) 0%, var(--statue-light) 45%, var(--statue-dark) 100%);
    opacity: 0.85;
  }
  .brand {
    position: absolute;
    left: 88px;
    top: 980px;
    width: 400px;
    text-align: center;
  }
  .brand-square {
    display: block;
    width: 64px;
    height: 64px;
    margin: 0 auto 50px;
    background: var(--brand-mark);
  }
  .firm-name {
    margin: 0;
    font-family: "Lato", "Helvetica", sans-serif;
    font-weight: 400;
    font-size: 54px;
    line-height: 1;
    letter-spacing: 5px;
    color: var(--brand-grey);
    white-space: nowrap;
  }
</style>
</head>
<body>
  <main class="postcard">
    <svg class="flag-art" viewBox="0 0 869 440" role="img" aria-label="Brush-painted American flag with stars and red and white stripes sweeping across the top">
      <defs>
        <linearGradient id="flagSweep" x1="0" y1="0" x2="1" y2="0.3">
          <stop offset="0" stop-color="var(--flag-blue)"/>
          <stop offset="0.38" stop-color="#6e6fb4"/>
          <stop offset="0.5" stop-color="var(--flag-white)"/>
          <stop offset="0.62" stop-color="#e0777b"/>
          <stop offset="1" stop-color="var(--flag-red)"/>
        </linearGradient>
      </defs>
      <path d="M0 0 H869 V255 C690 240 420 290 0 430 Z" fill="url(#flagSweep)"/>
    </svg>

    <h1 class="headline" aria-label="4th of July">
      <span class="headline-four">4</span>
      <span class="headline-th">TH</span>
      <span class="headline-of">OF</span>
      <span class="headline-july">JULY</span>
    </h1>
    <p class="subtitle">INDEPENDENCE DAY</p>

    <div class="statue" role="img" aria-label="Statue of Liberty holding a torch aloft and a tablet"></div>

    <div class="brand">
      <span class="brand-square" aria-hidden="true"></span>
      <p class="firm-name">HALDEN LAW</p>
    </div>
  </main>
</body>
</html>
```